Poem Handwritten by Veteran while in the jungle of Vietnam

My parents are celebrating their 50th wedding anniversary this year. I wanted to give them a very memorable gift. On my parents 2nd anniversary, my father was stationed in Vietnam. On that night he was in the jungle waiting till morning and wrote a poem to my mother using his pant leg as paper. I would like this poem to typographically designed to be framed and hung on the wall.

I have attached a picture of the poem below. It will need to be 11x14 when printed for framing. It would be great if there was background or artwork to make it more visually interesting, perhaps in a watercolor. My parents have a transitional style. I have attached some possible color schemes as well. Cool greens, blue, neutral grays, with hints of berries or highlights of yellow. These are just a guide, I would be open to your interpretations.

Thank you for your help. This will hopefully be a gift they will truly treasure as much as the poem itself.

Target Market(s)

My parents who are excited to be celebrating their 50th wedding anniversary. It should have a transitional, mature style.

Font styles to use
Serif
Script

Requirements
Must have
• The poem, typographically designed. There can be a mix of fonts, but legibility is critically important.
• Now that some designs have come through I wanted to give some more guidance of what I'm looking for. I want something that feels sophisticated and artistic.
Nice to have
• A background or art work, using the color schemes attached as a guide. I am really liking the designs that have a full color landscape artwork in the background. The fonts should be elegant and formal. I really like the romantic, muted colors. I had trouble finding similar projects online in the style I wanted until I cam across wedding invites. Those seem to be the most applicable. I've added pictures of some so you can get a sense of what I'm looking for. I am really liking the jungle foliage, starry skies or sunrises.
Should not have
• Cartoon caricatures, fonts that are too illegible when printed. I'm not liking anything whimsical. I don't like the very bright colors for this project.

```html
<!DOCTYPE html>
<html lang="en">
<head>
<meta charset="utf-8">
<title>Walter's Anniversary Poem</title>
<link href="https://fonts.googleapis.com/css2?family=Stardos+Stencil:wght@700&family=Alfa+Slab+One&family=Libre+Caslon+Text&display=swap" rel="stylesheet">
<style>
  :root {
    --page: #f4f3ef;
    --panel-top: #b0aa98;
    --panel-mid: #c9c6b8;
    --panel-bottom: #d9d7cd;
    --ink: #4a4943;
    --note: #ecebe4;
    --date-red: #8c1d1d;
    --title: #f6f5f0;
    --fabric-dark: #7f857a;
    --fabric-light: #a3a79b;
    --rose-tone: #a84a43;
    --leaf-tone: #5d7a52;
    --pencil-tone: #2b2b2a;
  }
  html, body {
    margin: 0;
    padding: 0;
    width: 1200px;
    height: 2521px;
    overflow: hidden;
    background: var(--page);
  }
  .poster {
    position: absolute;
    left: 224px;
    top: 160px;
    width: 753px;
    height: 2180px;
    overflow: hidden;
    background:
      radial-gradient(ellipse 70% 45% at 55% 38%, rgba(235,233,224,0.55), rgba(235,233,224,0) 70%),
      linear-gradient(180deg, var(--panel-top) 0%, var(--panel-mid) 45%, var(--panel-bottom) 100%);
  }
  .context-note {
    position: absolute;
    top: 42px;
    left: 78px;
    right: 78px;
    margin: 0;
    text-align: center;
    font-family: "Libre Caslon Text", serif;
    font-size: 12.5px;
    line-height: 20px;
    color: var(--note);
  }
  .date-line {
    position: absolute;
    top: 172px;
    left: 0;
    right: 0;
    margin: 0;
    text-align: center;
    font-family: "Alfa Slab One", serif;
    font-size: 27px;
    line-height: 36px;
    color: var(--date-red);
  }
  .title {
    position: absolute;
    top: 226px;
    left: 0;
    right: 0;
    margin: 0;
    text-align: center;
    font-family: "Stardos Stencil", serif;
    font-weight: 700;
    font-size: 92px;
    line-height: 76px;
    letter-spacing: 1px;
    color: var(--title);
  }
  .poem {
    position: absolute;
    top: 490px;
    left: 40px;
    width: 705px;
    text-align: center;
    font-family: "Libre Caslon Text", serif;
    font-size: 20px;
    line-height: 27.8px;
    color: var(--ink);
  }
  .stanza { margin: 0 0 27.6px; }
  .photo-fabric, .photo-rose, .photo-pencil { position: absolute; }
  .photo-fabric {
    left: 0;
    top: 1243px;
    width: 173px;
    height: 937px;
    background: linear-gradient(90deg, var(--fabric-dark), var(--fabric-light));
  }
  .photo-pencil {
    left: 3px;
    top: 2060px;
    width: 355px;
    height: 20px;
    background: var(--pencil-tone);
    opacity: 0.85;
  }
  .photo-rose {
    left: 565px;
    top: 1612px;
    width: 188px;
    height: 568px;
    background: linear-gradient(180deg, var(--rose-tone) 0%, var(--rose-tone) 22%, var(--leaf-tone) 45%, var(--leaf-tone) 100%);
    opacity: 0.8;
  }
</style>
</head>
<body>
  <main class="poster">
    <p class="context-note">This poem was written during the dark of night while on guard duty at LZ Professional in Viet Nam. I was at the time a 2nd Lieutenant in the Infantry. The date was July, 1970, our second anniversary. The original was penciled onto my army uniform, arranging only the key rhyming words without light to see</p>

    <p class="date-line">20 July 1970, Monday, LZ Professional</p>

    <h1 class="title">Walter’s<br>Anniversary<br>Poem</h1>

    <div class="poem">
      <p class="stanza">Life’s journey began with a challenge,<br>It was heralded far and near.<br>The road led on forever,<br>Its completion was known to be dear.</p>
      <p class="stanza">From the garden of light it proceeded,<br>To the valley of shadows it led.<br>Thorns and thistles adorned it,<br>Past abyss and crevice it sped.</p>
      <p class="stanza">The brave surged forward with courage,<br>The wise undaunted pressed on.<br>The mighty held high their banner,<br>We all awaited the dawn.</p>
      <p class="stanza">Though the pitfalls and hazards were many,<br>The pathway was clearly in view.<br>Straight and sure it glided,<br>Its course we knew to be true.</p>
      <p class="stanza">I knew you, Sweetheart, beforehand,<br>So precious and sweet were you.<br>Our moments of bliss were priceless,<br>Each day brought us joy anew.</p>
      <p class="stanza">The call to progression beckoned,<br>At last I would have my chance –<br>To clasp you to me forever,<br>And seal our divine romance.</p>
      <p class="stanza">I eagerly started the journey,<br>Though with sorrow, I left you behind.<br>With courage and faith I continued,<br>For I knew, that you later I’d find.</p>
      <p class="stanza">I diligently searched for you, Darling,<br>The roadway was both bleak and fair.<br>Though the years grew long in number,<br>I did not give up in despair.</p>
      <p class="stanza">At last in the distance I saw you,<br>So beautiful, lovely, and sweet!<br>Your attention I struggled to capture,<br>Your love I wrested to meet.</p>
      <p class="stanza">What rapture was mine in fulfillment,<br>As now together we stand.<br>To cherish and love each other,<br>While our plans and dreams expand.</p>
      <p class="stanza">I love you, Darling, forever,<br>My life you have made replete.<br>Our eternal mansion beckons<br>Your love has made it complete.</p>
    </div>

    <div class="photo-fabric" role="img" aria-label="Photo of a worn army uniform trouser leg with the line 'Your love has made it complete' handwritten in pencil"></div>
    <div class="photo-pencil" role="img" aria-label="Photo of a black pencil lying across the fabric"></div>
    <div class="photo-rose" role="img" aria-label="Photo of a single red rose with green stem and leaves"></div>
  </main>
</body>
</html>
```